3 banner themes for healthy foods supplements

Who you are
You are a top professional designer. You eat, sleep and breathe banners. You have them for breakfast, lunch and dinner. You have created so many high quality banners that you stopped counting.
Who we are
We are selling premium nutritional supplements.

Deliverables
We need to design 3 different banner themes, each in the following formats:
- Vertical rectangle: 240 x 400
- Mobile leaderboard: 320 x 50
- Banner: 468 x 60
- Leaderboard: 728 x 90
- Square: 250 x 250
- Small square: 200 x 200
- Large rectangle: 336 x 280
- Inline rectangle: 300 x 250
- Skyscraper: 120 x 600
- Wide skyscraper: 160 x 600
- Half-page: 300 x 600
- Large leaderboard: 970x90
- Large mobile banner: 320 x 100
- Billboard: 970 x 250
- Portrait: 300 x 1050

To give us a taste of your design skills, we invite you to submit one format (300 x 250) of each of the 3 different banner themes described below before we finally give you the green light and award you. Once awarded you should deliver all 3 themes with all above mentioned banner formats.

The final deliverable shall be editable .psd files.

Our products
The products we are advertising are organic, raw, vegan, premium nutritional supplements, such as algae powder, wheat grass powder and goji berries. The products stand to support a healthy life style. Please have a look at our shop. It is in German, but you get the gist. http://www.lumavera.-shop.example

The design
We would describe the style of the banners as follows:
- Premium
- Joyful
- White background
- Minimalistic

Each banner theme shall advertise the following messages about the products:
- Product name (chlorella algae powder , wheatgrass powder, goji berries)
- healthy
- 100 % vegan, raw and organic
- 100% natural
- premium product

Each of the above attributes can be represented with labels of different colours, similar to the attached sample files. We like the colour combination of the labels on this banner a lot.
All 3 themes shall contain our logo which you find attached to this job description. The logo shall be visible, but not too prominent.

The only difference between the 3 different themes shall be the product photo and the product name. All other elements on the banner shall be the same.

Theme A
This theme advertises algae powder, such as chlorella algae. The product photo is attached and should of course appear prominently on the banner.

Theme B
This theme advertises wheat grass powder. The product photo is attached and should of course appear prominently on the banner.

Theme C
This theme advertises goji berries. The product photo is attached and should of course appear prominently on the banner.

Target Market(s)

Health conscious people.

Industry/Entity Type

It Professional

Font styles to use
Sans Serif

Colors
00a990
a54499
f37122
fbed22
0692cd
9bcb3b
ffc214

Requirements
Must have
• - product image as per in the attachment
• - logo
• - bright, clear, joyful colors
Should not have
• - heavy dark colors
• - frame

```html
<!DOCTYPE html>
<html lang="en">
<head>
<meta charset="utf-8">
<title>Lumavera – Superfood Banner Themes</title>
<link rel="stylesheet" href="https://fonts.googleapis.com/css2?family=Arimo:ital,wght@0,700;1,700&display=swap">
<style>
  :root{
    --teal:#00a990;
    --purple:#a54499;
    --orange:#f37122;
    --yellow:#fbed22;
    --blue:#0692cd;
    --green:#9bcb3b;
    --gold:#ffc214;
    --ink:#333333;
    --white:#ffffff;
    --edge:#8a8a8a;
  }
  *{box-sizing:border-box;margin:0;padding:0}
  html,body{width:1200px;height:1200px;overflow:hidden;background:var(--white)}
  body{position:relative;font-family:"Arimo",Arial,sans-serif}

  .banner{
    position:absolute;left:409px;width:300px;height:250px;
    transform:scale(1.4118);transform-origin:0 0;
    background:var(--white);border:1px solid var(--edge);overflow:hidden;
  }
  .banner--chlorella{top:48px}
  .banner--wheatgrass{top:422px}
  .banner--goji{top:795px}

  .banner__backdrop{position:absolute;inset:0;width:100%;height:100%}

  .brand{
    position:absolute;left:10px;top:22px;display:flex;align-items:center;gap:5px;
    font-weight:700;font-size:16px;color:var(--teal);letter-spacing:.2px;
  }
  .brand__dot{width:14px;height:14px;border-radius:50%;background:var(--gold)}

  .shop-button{
    position:absolute;left:115px;top:10px;width:107px;height:30px;
    border-radius:6px;border:1px solid #7aa52c;
    background:linear-gradient(#b5dc62,var(--green) 55%,#86b92e);
    color:var(--white);font-weight:700;font-size:13px;
    display:flex;align-items:center;justify-content:center;
    text-shadow:0 1px 1px rgba(0,0,0,.25);
  }

  .product-name{
    position:absolute;left:0;top:78px;width:112px;
    color:var(--white);font-weight:700;font-size:19px;line-height:19px;text-align:right;
  }
  .product-name--short{top:88px;line-height:24px;width:100px}

  .product-photo{position:absolute;left:0;top:146px;width:95px;height:90px}
  .product-photo--chlorella{background:radial-gradient(ellipse at 55% 45%,#3d5c3a 0%,#2b4429 55%,rgba(43,68,41,0) 75%)}
  .product-photo--wheatgrass{background:radial-gradient(ellipse at 50% 55%,#c2c88a 0%,#aab66e 50%,rgba(170,182,110,0) 75%)}
  .product-photo--goji{background:radial-gradient(ellipse at 50% 55%,#d8452c 0%,#c0301c 50%,rgba(192,48,28,0) 75%)}

  .tag{
    position:absolute;display:flex;align-items:center;
    font-weight:700;color:var(--white);
    clip-path:polygon(0 0,calc(100% - 15px) 0,100% 15px,100% 100%,0 100%);
  }
  .tag::after{
    content:"";position:absolute;right:0;top:0;width:15px;height:15px;
    background:linear-gradient(45deg,#ffffff 0%,#c9c9c9 50%,transparent 50%);
  }
  .tag--healthy{left:142px;top:70px;width:151px;height:44px;background:var(--green);font-size:19px;padding-left:38px}
  .tag--vegan{left:135px;top:116px;width:158px;height:42px;background:var(--blue);font-size:12.5px;font-style:italic;line-height:14px;padding-left:6px}
  .tag--natural{left:110px;top:159px;width:173px;height:40px;background:var(--orange);font-size:19px;padding-left:6px}
  .tag--premium{left:88px;top:203px;width:184px;height:36px;background:linear-gradient(var(--yellow),#f3dc14);color:var(--ink);font-size:16px;padding-left:5px}
</style>
</head>
<body>

<!-- Theme A -->
<section class="banner banner--chlorella">
  <svg class="banner__backdrop" viewBox="0 0 300 250" aria-hidden="true">
    <defs>
      <linearGradient id="swoosh-a" x1="0" x2="1" y1="0" y2="0">
        <stop offset="0" stop-color="#fbed22"/><stop offset=".6" stop-color="#ffc214"/><stop offset="1" stop-color="#f39a22"/>
      </linearGradient>
    </defs>
    <path d="M120,78 C180,64 245,56 300,50 L300,250 L52,250 C88,205 118,160 140,100 Z" fill="#00a990"/>
    <path d="M0,66 C60,70 110,70 146,66 C140,112 124,150 100,176 C70,180 30,172 0,160 Z" fill="#a54499"/>
    <path d="M0,58 C100,74 200,62 300,40 L300,52 C200,72 100,82 0,70 Z" fill="url(#swoosh-a)"/>
    <path d="M0,50 C100,64 200,54 300,30 L300,40 C200,62 100,72 0,58 Z" fill="#efefef"/>
    <path d="M147,68 C140,130 105,195 55,250" fill="none" stroke="#ffc214" stroke-width="6"/>
  </svg>
  <div class="brand"><span class="brand__dot"></span>Lumavera</div>
  <div class="shop-button">SHOP NOW</div>
  <h2 class="product-name">Chlorella<br>Algae<br>Powder</h2>
  <div class="product-photo product-photo--chlorella" role="img" aria-label="Heap of dark green chlorella algae powder"></div>
  <div class="tag tag--healthy">Healthy</div>
  <div class="tag tag--vegan">100% vegan, Raw<br>&amp; Organic</div>
  <div class="tag tag--natural">100% Natural</div>
  <div class="tag tag--premium">Premium Product</div>
</section>

<!-- Theme B -->
<section class="banner banner--wheatgrass">
  <svg class="banner__backdrop" viewBox="0 0 300 250" aria-hidden="true">
    <defs>
      <linearGradient id="swoosh-b" x1="0" x2="1" y1="0" y2="0">
        <stop offset="0" stop-color="#fbed22"/><stop offset=".6" stop-color="#ffc214"/><stop offset="1" stop-color="#f39a22"/>
      </linearGradient>
    </defs>
    <path d="M120,78 C180,64 245,56 300,50 L300,250 L52,250 C88,205 118,160 140,100 Z" fill="#00a990"/>
    <path d="M0,66 C60,70 110,70 146,66 C140,112 124,150 100,176 C70,180 30,172 0,160 Z" fill="#a54499"/>
    <path d="M0,58 C100,74 200,62 300,40 L300,52 C200,72 100,82 0,70 Z" fill="url(#swoosh-b)"/>
    <path d="M0,50 C100,64 200,54 300,30 L300,40 C200,62 100,72 0,58 Z" fill="#efefef"/>
    <path d="M147,68 C140,130 105,195 55,250" fill="none" stroke="#ffc214" stroke-width="6"/>
  </svg>
  <div class="brand"><span class="brand__dot"></span>Lumavera</div>
  <div class="shop-button">SHOP NOW</div>
  <h2 class="product-name">Wheat<br>Grass<br>Powder</h2>
  <div class="product-photo product-photo--wheatgrass" role="img" aria-label="Heap of pale green wheat grass powder"></div>
  <div class="tag tag--healthy">Healthy</div>
  <div class="tag tag--vegan">100% vegan, Raw<br>&amp; Organic</div>
  <div class="tag tag--natural">100% Natural</div>
  <div class="tag tag--premium">Premium Product</div>
</section>

<!-- Theme C -->
<section class="banner banner--goji">
  <svg class="banner__backdrop" viewBox="0 0 300 250" aria-hidden="true">
    <defs>
      <linearGradient id="swoosh-c" x1="0" x2="1" y1="0" y2="0">
        <stop offset="0" stop-color="#fbed22"/><stop offset=".6" stop-color="#ffc214"/><stop offset="1" stop-color="#f39a22"/>
      </linearGradient>
    </defs>
    <path d="M120,78 C180,64 245,56 300,50 L300,250 L52,250 C88,205 118,160 140,100 Z" fill="#00a990"/>
    <path d="M0,66 C60,70 110,70 146,66 C140,112 124,150 100,176 C70,180 30,172 0,160 Z" fill="#a54499"/>
    <path d="M0,58 C100,74 200,62 300,40 L300,52 C200,72 100,82 0,70 Z" fill="url(#swoosh-c)"/>
    <path d="M0,50 C100,64 200,54 300,30 L300,40 C200,62 100,72 0,58 Z" fill="#efefef"/>
    <path d="M147,68 C140,130 105,195 55,250" fill="none" stroke="#ffc214" stroke-width="6"/>
  </svg>
  <div class="brand"><span class="brand__dot"></span>Lumavera</div>
  <div class="shop-button">SHOP NOW</div>
  <h2 class="product-name product-name--short">Goji<br>Barries</h2>
  <div class="product-photo product-photo--goji" role="img" aria-label="Pile of red dried goji berries"></div>
  <div class="tag tag--healthy">Healthy</div>
  <div class="tag tag--vegan">100% vegan, Raw<br>&amp; Organic</div>
  <div class="tag tag--natural">100% Natural</div>
  <div class="tag tag--premium">Premium Product</div>
</section>

</body>
</html>
```